Honey jar label for small US farm

My daughters have 6 beehives and will be producing 300-400 jars of honey this season that they plan to sell at the farmers' market.
We are looking for a label design for small honey jars.
Label size:  1.5 inches high and 3 inches wide.
The label will be a simple RECTANGLE (no special cut)
We would like a playful look but upscale enough. We don't think that flowers or bees add anything. We like cleaner looks but not cold.
Maybe one could also represent the 3 sisters somewhere on the label. As elegant stick figures maybe?
One could also imagine a design where the label is black and the text/images are white to add some dramatic effect. The jar lid is black.
The honey is raw, un-pasturized, straight from the beehive.

Target Market(s)
Farm stand, sold by the 3 sisters who are 11, 9 and 6
Industry/Entity Type
Food Production
Colors
Designer to choose colors to be used in the design.
Requirements
Must have
- Name (means three sisters in English): Clos Ardent
- What it is: Berkshire Raw Honey
- Net weight: 3.75oz (110ml)
- Location: Elmhollow, MA
- Text on one of the sides: Sister to sister we will always be, a couple of nuts off the family tree!
- Note that the jar is an hexagon. See the attached STOCK photo.
- Therefore, a little more than 1 inch is on the front facing, and 0.75 inches on each sides.

Nice to have
- The design should be elegant (but not ornate), but clean. Inviting and fun.
- No need for bees or flowers which would not make it look upscale.
- No gold or "over the top" fancy. Modern but not cold.
- Remember that this is a honey brand for 3 young sisters. Something playful but upscale would work too.
- Not sure about color codes. We are quite happy staying in grey scales, but a little bit of colour might work too.

Should not have
- No UPC code needed

```html
<!DOCTYPE html>
<html lang="en">
<head>
<meta charset="utf-8">
<title>Clos Ardent – Berkshire Raw Honey Label</title>
<link href="https://fonts.googleapis.com/css2?family=Crimson+Text&family=Roboto+Condensed:wght@400&display=swap" rel="stylesheet">
<style>
  :root {
    --page: #ffffff;
    --label: #0b0b0b;
    --ink: #f2f2f2;
    --ink-soft: #8a8a8a;
    --ink-dim: #6a6a6a;
    --fold: #1c1c1c;
    --art: #2a2a2a;
  }
  html, body {
    margin: 0;
    width: 1200px;
    height: 639px;
    overflow: hidden;
    background: var(--page);
  }
  .canvas {
    position: relative;
    width: 1200px;
    height: 639px;
    display: flex;
    align-items: center;
    justify-content: center;
  }
  .label {
    width: 900px;
    height: 450px;
    background: var(--label);
    display: grid;
    grid-template-columns: 240px 420px 240px;
  }
  .panel {
    position: relative;
    box-sizing: border-box;
  }
  .panel--front {
    border-left: 1px solid var(--fold);
    border-right: 1px solid var(--fold);
    text-align: center;
    padding-top: 44px;
  }
  .brand-name {
    margin: 0;
    font-family: "Crimson Text", serif;
    font-weight: 400;
    font-size: 72px;
    line-height: 1;
    color: var(--ink);
  }
  .product-name {
    margin: 22px 0 0;
    font-family: "Crimson Text", serif;
    font-size: 30px;
    color: var(--ink);
  }
  .sisters-art {
    display: block;
    margin: 34px auto 0;
    width: 300px;
    height: 220px;
  }
  .panel--left {
    display: flex;
    align-items: center;
    justify-content: center;
  }
  .motto {
    margin: 0 0 60px;
    font-family: "Roboto Condensed", sans-serif;
    font-size: 22px;
    line-height: 1.75;
    color: var(--ink-soft);
    text-align: center;
  }
  .panel--right {
    font-family: "Roboto Condensed", sans-serif;
    color: var(--ink-dim);
  }
  .claims {
    list-style: none;
    margin: 0;
    padding: 90px 0 0 42px;
    font-size: 15px;
    text-transform: uppercase;
    line-height: 1.35;
  }
  .claims li { margin-bottom: 22px; }
  .claims li::before { content: "- "; }
  .location {
    position: absolute;
    left: 30px;
    bottom: 52px;
    font-size: 12px;
  }
  .net-weight {
    position: absolute;
    right: 26px;
    bottom: 52px;
    font-size: 12px;
    line-height: 1.6;
    text-align: left;
  }
</style>
</head>
<body>
<main class="canvas">
  <section class="label">
    <div class="panel panel--left">
      <p class="motto">Sister to sister<br>we will always be,<br>a couple of nuts<br>off the family tree!</p>
    </div>

    <div class="panel panel--front">
      <h1 class="brand-name">Clos Ardent</h1>
      <p class="product-name">Berkshire Raw Honey</p>
      <svg class="sisters-art" role="img" aria-label="White line illustration of three young sisters playing jump rope" viewBox="0 0 300 220">
        <rect width="300" height="220" rx="6" fill="var(--art)"/>
      </svg>
    </div>

    <div class="panel panel--right">
      <ul class="claims">
        <li>The honey is raw</li>
        <li>Un-pasturized</li>
        <li>Straight from<br>&nbsp;&nbsp;the beehive</li>
      </ul>
      <span class="location">Elmhollow, MA</span>
      <span class="net-weight">Net weight<br>3.75oz (110ml)</span>
    </div>
  </section>
</main>
</body>
</html>
```